Music Festival Business Cards

The Lantern Gathering
Produced by Bramblewood Sound Collective LLC
New music festival in Arkansas.

Target Market(s)

18-35 year olds

Industry/Entity Type

Festival

Contact Information for Business Card

We are a 5-partner team producing a music festival in Arkansas. We need slick business cards, and I want them to be square.

Requirements
Must have
• I NEED THESE TO BE IN SQUARE SIZE - 2x2 or 2.5x2.5... please not regular size.
• I need www.lanternmeet.example as the link to website.

```html
<!DOCTYPE html>
<html lang="en">
<head>
<meta charset="utf-8">
<title>The Lantern Gathering – Square Business Card</title>
<link href="https://fonts.googleapis.com/css2?family=Michroma&family=Open+Sans:wght@400;700&display=swap" rel="stylesheet">
<style>
  :root {
    --bg: #4a3f37;
    --teal: #49c2cc;
    --ink: #080808;
    --white: #f4f4f4;
  }
  * { margin: 0; padding: 0; box-sizing: border-box; }
  html, body { width: 1200px; height: 1200px; overflow: hidden; background: var(--bg); }
  .canvas {
    width: 1200px; height: 1200px;
    display: flex; flex-direction: row; align-items: center; justify-content: center; gap: 40px;
  }
  .card {
    position: relative; width: 540px; height: 540px; overflow: hidden;
    box-shadow: 0 10px 24px rgba(0,0,0,0.35);
  }
  /* Front */
  .card-front { background: var(--teal); display: flex; align-items: center; justify-content: center; }
  .front-brand {
    font-family: "Michroma", sans-serif; font-size: 30px; color: var(--ink);
    letter-spacing: 1px; text-align: center; line-height: 1.4;
  }
  /* Back */
  .card-back { background: var(--ink); }
  .brand {
    position: absolute; left: 44px; top: 64px;
    font-family: "Michroma", sans-serif; font-size: 26px; color: var(--teal);
    letter-spacing: 1px; line-height: 1.35;
  }
  .person { position: absolute; left: 44px; top: 196px; font-family: "Open Sans", sans-serif; }
  .person-name { font-size: 28px; font-weight: 700; color: var(--teal); line-height: 1.15; }
  .person-role { font-size: 18px; color: var(--white); }
  .address {
    position: absolute; right: 44px; top: 200px; text-align: right;
    font-family: "Open Sans", sans-serif; font-size: 16px; color: var(--white); line-height: 1.45;
  }
  .address svg { vertical-align: -2px; margin-left: 6px; }
  .divider { position: absolute; left: 44px; right: 44px; top: 278px; height: 1px; background: var(--teal); opacity: 0.7; }
  .contacts {
    position: absolute; left: 44px; top: 300px; list-style: none;
    font-family: "Open Sans", sans-serif; font-size: 18px; color: var(--white); line-height: 1.6;
  }
  .contacts li { display: flex; align-items: center; gap: 12px; }
  .contacts svg { flex: none; width: 20px; }
  .band { position: absolute; left: 0; bottom: 0; width: 100%; height: 52px; }
</style>
</head>
<body>
<main class="canvas">
  <section class="card card-front" aria-label="Card front">
    <p class="front-brand">THE LANTERN<br>GATHERING</p>
  </section>

  <section class="card card-back" aria-label="Card back">
    <p class="brand">THE LANTERN<br>GATHERING</p>

    <div class="person">
      <p class="person-name">ROWAN ELLERY</p>
      <p class="person-role">Director</p>
    </div>

    <p class="address">Dummy city<svg width="12" height="16" viewBox="0 0 14 18"><path d="M7 1a6 6 0 0 0-6 6c0 4.5 6 10 6 10s6-5.5 6-10a6 6 0 0 0-6-6z" fill="none" stroke="var(--teal)" stroke-width="2"/><circle cx="7" cy="7" r="2" fill="var(--teal)"/></svg><br>Dummy Country Land</p>

    <div class="divider"></div>

    <ul class="contacts">
      <li><svg height="18" viewBox="0 0 20 20"><path d="M5 2l3 4-2 2c1 2 3 4 5 5l2-2 4 3-2 3C9 17 3 11 2 4z" fill="var(--teal)"/></svg>1-555-014-2290</li>
      <li><svg height="18" viewBox="0 0 20 20"><circle cx="10" cy="10" r="8" fill="none" stroke="var(--teal)" stroke-width="2"/><path d="M2 10h16M10 2c-4 4-4 12 0 16M10 2c4 4 4 12 0 16" fill="none" stroke="var(--teal)" stroke-width="1.5"/></svg>www.lanternmeet.example</li>
      <li><svg height="15" viewBox="0 0 22 16"><rect x="1" y="1" width="20" height="14" fill="var(--teal)"/><path d="M1 1l10 8 10-8" fill="none" stroke="var(--ink)" stroke-width="1.5"/></svg>rowan@lanternmeet.example</li>
    </ul>

    <svg class="band" viewBox="0 0 540 52" preserveAspectRatio="none" aria-hidden="true">
      <polygon points="0,52 0,34 336,34 336,0 540,0 540,52" fill="var(--teal)"/>
      <polygon points="318,34 332,34 352,52 338,52" fill="var(--ink)"/>
    </svg>
  </section>
</main>
</body>
</html>
```